Non fiction leadership Book Cover design needed for “Hold Fast: Forge A Steady Track”

I need a front cover design for a new book 6 X 9 traditional non-fiction book.

Title: "Hold FAST - Forge A Steady Track"

The subtitle is not finalized- so use 2 lines of smaller dummy text

My brand guide is attached (please use the tan color sparingly)

I'd like to see FAST look like it is in motion and "flying" across the page

Need CREATIVE designs and options

Do not want my picture on the front cover - I do want it on the back cover.

On the front cover I’d like to see creative use of font to create movement on “FAST”

Target Market(s)

Business leaders

Industry/Entity Type

Aviation

Font styles to use
Other font styles liked:
• See style guide- can add additional font (modern script or san serif)

Colors
0054AA
0677BA
7BADD7
CADEEF
E8F1F8
EB3D1F
EC4F4E
F09395
F8D3D4
FCEDEE

Requirements
Must have
• Creative font use, using perspective to create movement/motion on FAST
Should not have
• My picture on the front cover- my picture should be on the back cover

```html
<!DOCTYPE html>
<html lang="en">
<head>
<meta charset="utf-8">
<title>Hold FAST - Forge A Steady Track</title>
<link rel="stylesheet" href="https://fonts.googleapis.com/css2?family=Bebas+Neue&family=Montserrat:wght@700;800&display=swap">
<style>
  :root {
    --sky-top: #0054AA;
    --sky-mid: #285B8C;
    --sky-bottom: #0B78BA;
    --ribbon-bright: #E81F25;
    --ribbon-deep: #A11C2A;
    --ribbon-left: #D62027;
    --white: #FFFFFF;
    --yellow: #F3E61F;
    --ink: #000000;
  }
  * { margin: 0; padding: 0; box-sizing: border-box; }
  html, body { width: 800px; height: 1200px; overflow: hidden; background: var(--sky-top); }
  .cover { position: relative; width: 800px; height: 1200px; display: block; }
  .title-main, .title-kicker, .title-tail { font-family: "Montserrat", sans-serif; font-weight: 700; }
  .title-main, .title-kicker, .title-dash { fill: var(--white); }
  .title-tail { fill: var(--yellow); }
  .ribbon-letter { font-family: "Montserrat", sans-serif; font-weight: 700; fill: var(--white); font-size: 136px; }
  .subtitle, .author { font-family: "Bebas Neue", sans-serif; letter-spacing: 4px; }
  .subtitle { font-size: 50px; }
  .subtitle .plain { fill: var(--white); }
  .subtitle .accent { fill: var(--yellow); }
  .author { font-size: 66px; fill: var(--ink); letter-spacing: 5px; }
  .divider { fill: var(--white); }
</style>
</head>
<body>
<svg class="cover" viewBox="0 0 800 1200" xmlns="http://www.w3.org/2000/svg">
  <defs>
    <linearGradient id="sky" x1="0" y1="0" x2="0" y2="1">
      <stop offset="0" stop-color="var(--sky-top)"/>
      <stop offset="0.5" stop-color="var(--sky-mid)"/>
      <stop offset="1" stop-color="var(--sky-bottom)"/>
    </linearGradient>
    <linearGradient id="ribbon-shade" x1="0" y1="0" x2="1" y2="0">
      <stop offset="0" stop-color="var(--ribbon-left)"/>
      <stop offset="0.35" stop-color="var(--ribbon-deep)"/>
      <stop offset="0.6" stop-color="#B51E28"/>
      <stop offset="0.88" stop-color="var(--ribbon-bright)"/>
      <stop offset="1" stop-color="#D91F26"/>
    </linearGradient>
  </defs>

  <rect class="background" width="800" height="1200" fill="url(#sky)"/>

  <text class="title-main" x="74" y="255" font-size="236" textLength="597" lengthAdjust="spacingAndGlyphs">HOLD</text>

  <path class="ribbon" fill="url(#ribbon-shade)"
        d="M0 292 C80 286 180 290 300 330 C420 372 520 400 600 402 C680 404 740 395 800 380
           L800 537 C740 545 680 550 600 545 C500 540 420 510 300 470 C180 430 100 430 0 437 Z"/>

  <g class="ribbon-word">
    <text class="ribbon-letter" transform="translate(172 432) rotate(12)">F</text>
    <text class="ribbon-letter" transform="translate(290 470) rotate(9)">A</text>
    <text class="ribbon-letter" transform="translate(420 497) rotate(5)">S</text>
    <text class="ribbon-letter" transform="translate(530 521)">T</text>
  </g>

  <rect class="title-dash" x="120" y="612" width="41" height="19"/>
  <text class="title-kicker" x="198" y="660" font-size="132" textLength="340" lengthAdjust="spacingAndGlyphs">Forge</text>
  <rect class="title-dash" x="576" y="612" width="41" height="19"/>

  <text class="title-tail" x="76" y="756" font-size="86" textLength="594" lengthAdjust="spacingAndGlyphs">A Steady Track</text>

  <text class="subtitle" x="104" y="879" textLength="565" lengthAdjust="spacing">
    <tspan class="accent">UNLOCK YOUR</tspan><tspan class="plain"> INNER POTENTIAL</tspan>
  </text>
  <text class="subtitle" x="139" y="936" textLength="483" lengthAdjust="spacing">
    <tspan class="plain">AND SOAR TO </tspan><tspan class="accent">NEW HEIGHTS</tspan>
  </text>

  <rect class="divider" x="297" y="1005" width="151" height="11"/>

  <text class="author" x="201" y="1141" textLength="344" lengthAdjust="spacing">AUTHOR NAME</text>
</svg>
</body>
</html>
```